Clarivane Label Design

We need a label design for our cream dispenser. Its a cream against acne called Clarivane, Works with its active ingredients of silver and oxygen. We are looking for a flashy / colorful and modern design .

Target Market(s)

young people / People with acne

Industry/Entity Type

Skin Care Product

Colors

Designer to choose colors to be used in the design.

Requirements
Must have
• be modern, Colours
• -THE DESIGN NEEDS TO BE 10,7x7 , ITS 1 BIG STICKER THAT RAPS AROUND THE BOTTLE

```html
<!DOCTYPE html>
<html lang="en">
<head>
<meta charset="utf-8">
<title>Clarivane Label</title>
<link rel="stylesheet" href="https://fonts.googleapis.com/css2?family=Lexend:wght@300;400;500&display=swap">
<style>
  :root {
    --page: #ffffff;
    --teal: #24bcc2;
    --ink: #3a3d42;
    --silver-light: #f4f5f6;
    --silver-mid: #d3d5d8;
    --silver-dark: #a9acb1;
    --cream: #f3f3f3;
    --white: #ffffff;
  }
  html, body {
    margin: 0;
    padding: 0;
    width: 1200px;
    height: 1200px;
    overflow: hidden;
    background: var(--page);
  }
  .canvas {
    position: relative;
    width: 1200px;
    height: 1200px;
    background: var(--page);
  }
  .label {
    position: absolute;
    left: 370px;
    top: 140px;
    width: 460px;
    height: 920px;
    box-shadow: 0 6px 24px rgba(0,0,0,0.08);
  }
  .brand-name {
    font-family: "Lexend", sans-serif;
    font-weight: 500;
    font-size: 46px;
    letter-spacing: 4px;
    fill: var(--teal);
  }
  .product-line {
    font-family: "Lexend", sans-serif;
    font-weight: 400;
    font-size: 38px;
    fill: var(--teal);
  }
  .tagline {
    font-family: "Lexend", sans-serif;
    font-weight: 400;
    font-size: 23px;
    fill: var(--white);
  }
  .volume {
    font-family: "Lexend", sans-serif;
    font-weight: 300;
    font-size: 15px;
    fill: var(--white);
  }
</style>
</head>
<body>
<main class="canvas">
  <svg class="label" viewBox="0 0 435 870" xmlns="http://www.w3.org/2000/svg">
    <defs>
      <linearGradient id="silverPanel" x1="0" y1="0" x2="1" y2="0">
        <stop offset="0" stop-color="var(--silver-light)"/>
        <stop offset="0.55" stop-color="var(--white)"/>
        <stop offset="1" stop-color="var(--silver-mid)"/>
      </linearGradient>
      <linearGradient id="silverBand" x1="0" y1="0" x2="1" y2="0">
        <stop offset="0" stop-color="var(--silver-dark)"/>
        <stop offset="0.5" stop-color="var(--silver-light)"/>
        <stop offset="1" stop-color="var(--silver-dark)"/>
      </linearGradient>
      <radialGradient id="creamTone" cx="0.5" cy="0.4" r="0.6">
        <stop offset="0" stop-color="var(--white)"/>
        <stop offset="1" stop-color="#e4e5e7"/>
      </radialGradient>
    </defs>

    <!-- base -->
    <rect class="label-base" x="0" y="0" width="435" height="870" fill="var(--white)"/>

    <!-- top silver panel -->
    <path class="top-panel" d="M0 0 H435 V235 C300 245 90 280 0 330 Z" fill="url(#silverPanel)"/>
    <path class="top-band" d="M0 330 C90 280 300 245 435 235 V250 C300 258 110 290 0 345 Z" fill="url(#silverBand)"/>

    <!-- brand -->
    <text class="brand-name" x="217.5" y="205" text-anchor="middle">Clarivane</text>

    <!-- product line -->
    <text class="product-line" x="225" y="374" text-anchor="middle">ACNE REPAIR</text>
    <text class="product-line" x="225" y="426" text-anchor="middle">&amp; CARE</text>

    <!-- cream visual -->
    <ellipse class="cream-visual" cx="225" cy="522" rx="118" ry="52" fill="url(#creamTone)" role="img" aria-label="Swirl of white acne cream"/>

    <!-- bottom teal panel -->
    <path class="bottom-band" d="M0 612 C130 610 330 580 435 548 V565 C330 598 130 628 0 630 Z" fill="url(#silverBand)"/>
    <path class="bottom-panel" d="M0 630 C130 628 330 598 435 565 V870 H0 Z" fill="var(--teal)"/>

    <!-- bottom text -->
    <text class="tagline" x="217.5" y="733" text-anchor="middle">LOREM IPSUM</text>
    <text class="tagline" x="217.5" y="764" text-anchor="middle">DOLOR SIT AMET</text>
    <text class="volume" x="217.5" y="808" text-anchor="middle">100 ML</text>
  </svg>
</main>
</body>
</html>
```